Awesome Digital Ad Design – Pellucid Adreach

I am going to be setting up a Pellucid Adreach ad campaign I need creatives for.

Several sizes are needed in the end, however, please submit your design concept in the following 2 sizes to start:
Medium rectangle: 300X250
Leaderboard: 728X90

Original artwork/design files and images used expected upon payment and as part of the final delivery.

Ads should match our company brand and the information on this webpage: http://www.harborlyneworks.com/real-estate-marketing/
SEE MORE INSTRUCTIONS IN ATTACHED WORD DOC
Updates

Target Market(s)

Business-To-Business Audience –Real Estate Company Executives (Presidents/VPs/Owners/CEOs/Sales Managers).

Industry/Entity Type

Real Estate

Font styles to use
Sans Serif

Requirements
Must have
• Copy should be minimal words, billboard like. Please use real photos/images that would appeal to real estate high-level decision-maker executives.
Should not have
• No cartoons or graphics

```html
<!DOCTYPE html>
<html lang="en">
<head>
<meta charset="utf-8">
<title>Harborlyne Works – Display Ad Concepts</title>
<link href="https://fonts.googleapis.com/css2?family=Poppins:wght@400;500;600&display=swap" rel="stylesheet">
<style>
  :root {
    --stage-light: #5f7078;
    --stage-dark: #1b2a30;
    --label: #e6ecef;
    --ink-dark: #0b1119;
    --photo-light: #3d6a8d;
    --photo-mid: #1f3b55;
    --photo-deep: #0f1d2c;
    --panel: #e9f4f8;
    --panel-edge: #2e7fae;
    --white: #ffffff;
    --gold: #e9cf8b;
    --orange: #ec6a1a;
    --orange-light: #f78a3a;
    --strip-steel: #7d95a8;
    --strip-maroon: #7a2a3e;
    --strip-khaki: #c9b98a;
    --strip-slate: #4f6b80;
    --logo-ink: #2a3440;
  }
  * { box-sizing: border-box; margin: 0; padding: 0; }
  html, body { width: 1200px; height: 800px; overflow: hidden; }
  body {
    font-family: "Poppins", sans-serif;
    background: radial-gradient(ellipse 900px 700px at 1000px 30px, var(--stage-light), var(--stage-dark));
    position: relative;
  }
  .size-label {
    position: absolute; width: 200px; text-align: center;
    color: var(--label); font-size: 17px; font-weight: 400;
  }
  .ad {
    position: absolute; overflow: hidden;
    background: var(--ink-dark);
    border: 1px solid #0a0f14;
    box-shadow: 0 6px 10px rgba(0,0,0,.45);
  }
  .ad-photo {
    position: absolute;
    background: linear-gradient(90deg, var(--photo-mid), var(--photo-light) 45%, var(--photo-mid) 70%, var(--photo-deep));
  }
  .ad-logo-panel { position: absolute; left: 0; top: 0; }
  .brand-name {
    position: absolute; color: var(--logo-ink);
    font-weight: 500; line-height: 1.15; text-align: center;
  }
  .color-strip { position: absolute; left: 0; display: flex; }
  .color-strip span { display: block; height: 100%; }
  .steel { background: var(--strip-steel); }
  .maroon { background: var(--strip-maroon); }
  .khaki { background: var(--strip-khaki); }
  .slate { background: var(--strip-slate); }
  .deep { background: var(--photo-deep); }
  .headline {
    position: absolute; text-align: center; line-height: 1; white-space: nowrap;
  }
  .headline-top { color: var(--white); font-weight: 600; }
  .headline-main { color: var(--gold); font-weight: 600; }
  .subline { color: var(--white); font-weight: 400; }
  .cta {
    position: absolute; display: flex; align-items: center; justify-content: center;
    background: linear-gradient(180deg, var(--orange-light), var(--orange));
    color: var(--white); font-weight: 500; border-radius: 3px;
    box-shadow: 0 1px 2px rgba(0,0,0,.5);
  }

  /* Medium rectangle */
  .ad-rectangle { left: 450px; top: 131px; width: 300px; height: 250px; }
  .ad-rectangle .ad-photo { left: 0; top: 0; width: 300px; height: 110px; }
  .ad-rectangle .brand-name { left: 4px; top: 38px; width: 72px; font-size: 10px; }
  .ad-rectangle .color-strip { top: 110px; width: 300px; height: 16px; }
  .ad-rectangle .headline { left: 0; width: 298px; }
  .ad-rectangle .headline-top { top: 133px; font-size: 20px; }
  .ad-rectangle .headline-main { top: 154px; font-size: 28px; }
  .ad-rectangle .subline { top: 183px; font-size: 12.5px; }
  .ad-rectangle .cta { left: 91px; top: 204px; width: 118px; height: 36px; font-size: 14px; }

  /* Leaderboard */
  .ad-leaderboard { left: 236px; top: 477px; width: 728px; height: 90px; }
  .ad-leaderboard .ad-photo { left: 0; top: 0; width: 728px; height: 80px; }
  .ad-leaderboard .brand-name { left: 8px; top: 29px; width: 76px; font-size: 10px; }
  .ad-leaderboard .color-strip { top: 80px; width: 728px; height: 10px; }
  .ad-leaderboard .headline { left: 140px; width: 250px; }
  .ad-leaderboard .headline-top { top: 9px; font-size: 18px; }
  .ad-leaderboard .headline-main { top: 28px; font-size: 27px; }
  .ad-leaderboard .subline { top: 58px; font-size: 12.5px; }
  .ad-leaderboard .cta { left: 591px; top: 23px; width: 118px; height: 37px; font-size: 14px; }
</style>
</head>
<body>

  <p class="size-label" style="left:500px; top:94px;">300x250</p>

  <section class="ad ad-rectangle" aria-label="Medium rectangle ad">
    <div class="ad-photo" role="img" aria-label="Photo of an executive in a suit drawing with a blue marker beside a glowing walking figure"></div>
    <svg class="ad-logo-panel" width="110" height="112" viewBox="0 0 110 112" aria-hidden="true">
      <polygon points="0,0 56,0 96,64 0,112" fill="var(--panel-edge)"/>
      <polygon points="0,0 50,0 102,56 0,110" fill="var(--panel)"/>
    </svg>
    <p class="brand-name">Harborlyne Works</p>
    <div class="color-strip">
      <span class="steel" style="width:12px"></span>
      <span class="maroon" style="width:64px"></span>
      <span class="khaki" style="width:67px"></span>
      <span class="slate" style="width:64px"></span>
      <span class="deep" style="width:61px"></span>
      <span class="maroon" style="width:32px"></span>
    </div>
    <p class="headline headline-top">CLIENT FOLLOW-UP</p>
    <p class="headline headline-main">MADE SIMPLE</p>
    <p class="headline subline">Virtually No Cost To Your Company!</p>
    <a class="cta">LEARN MORE</a>
  </section>

  <p class="size-label" style="left:500px; top:450px;">728x90</p>

  <section class="ad ad-leaderboard" aria-label="Leaderboard ad">
    <div class="ad-photo" role="img" aria-label="Photo of a glowing walking figure and an executive in a suit holding a blue marker"></div>
    <svg class="ad-logo-panel" width="140" height="82" viewBox="0 0 140 82" aria-hidden="true">
      <polygon points="0,0 98,0 136,41 98,80 0,80" fill="var(--panel-edge)"/>
      <polygon points="0,0 90,0 128,41 90,80 0,80" fill="var(--panel)"/>
    </svg>
    <p class="brand-name">Harborlyne Works</p>
    <div class="color-strip">
      <span class="steel" style="width:51px"></span>
      <span class="maroon" style="width:54px"></span>
      <span class="khaki" style="width:54px"></span>
      <span class="slate" style="width:54px"></span>
      <span class="steel" style="width:54px"></span>
      <span class="maroon" style="width:54px"></span>
      <span class="khaki" style="width:54px"></span>
      <span class="steel" style="width:54px"></span>
      <span class="slate" style="width:54px"></span>
      <span class="deep" style="width:49px"></span>
      <span class="maroon" style="width:55px"></span>
      <span class="khaki" style="width:49px"></span>
      <span class="slate" style="width:54px"></span>
      <span class="steel" style="width:38px"></span>
    </div>
    <p class="headline headline-top">CLIENT FOLLOW-UP</p>
    <p class="headline headline-main">MADE SIMPLE</p>
    <p class="headline subline">Virtually No Cost To Your Company!</p>
    <a class="cta">LEARN MORE</a>
  </section>

</body>
</html>
```